Postcard needed for expert witness service

Looking for a professional postcard that will be mailed to personal injury lawyers / law firms to introduce my expert witness services.

Target Market(s)

Law firms, personal injury lawyers

Industry/Entity Type

Expert witness, law

Font styles to use
Sans Serif

Requirements
Must have
• Logo: The Frost Counsel [Main Heading]Do you handle snow and ice related slip and falls? Darrel is one of the top snow industry experts in the country! [Following should be in a list type fashion, possibly bulleted]Darrel's credentials: Accredited Winter Practitioner (AWP), past WRTA board member and chair, former ISO 9001 certified snow company owner , 32 years in the industry. (555) 284-3917 NOTES: Postcard will be 4" x 6" Please use both sides however must have room for labels and stamp
Should not have
• Wouldn't suggest using both photos on same side. Honestly, feel free to only use one of the slip and fall photos if it works out better. Thanks!

```html
<!DOCTYPE html>
<html lang="en">
<head>
<meta charset="utf-8">
<title>The Frost Counsel – Postcard</title>
<link rel="stylesheet" href="https://fonts.googleapis.com/css2?family=Poppins:ital,wght@0,300;0,400;0,800;1,400&display=swap">
<style>
  :root{
    --stage:#5e5e5e;
    --ink:#131112;
    --ink-soft:#1e1c1d;
    --ice:#7fcfe3;
    --white:#ffffff;
    --rule:#9a9a9a;
    --photo-a:#8b8985;
    --photo-b:#3a3538;
    --photo-c:#d7d8da;
  }
  *{margin:0;padding:0;box-sizing:border-box}
  html,body{width:1200px;height:1200px;overflow:hidden;background:var(--stage);font-family:"Poppins",sans-serif}
  .card{position:absolute;overflow:hidden}
  .front{left:81px;top:82px;width:746px;height:497px;background:var(--ink)}
  .back{left:376px;top:630px;width:753px;height:502px;background:var(--white)}
  .shape{position:absolute;inset:0;width:100%;height:100%}
  .photo{position:absolute;left:0;top:0;width:520px;height:497px;
    background:linear-gradient(160deg,var(--photo-c) 0%,var(--photo-a) 30%,var(--photo-b) 55%,#4a5f78 75%,var(--photo-c) 100%)}
  .brand{position:absolute;color:var(--white);font-weight:300;font-size:25px;letter-spacing:1px;line-height:1.15;text-transform:uppercase}
  .front .brand{left:42px;top:30px}
  .back .brand{left:45px;top:42px}
  .headline{position:absolute;right:26px;top:36px;text-align:right;font-size:42px;line-height:46px;color:var(--white)}
  .headline .light{font-weight:300;display:block}
  .headline .bold{font-weight:800;display:block;letter-spacing:-0.5px}
  .headline .ice{color:var(--ice)}
  .intro{position:absolute;right:27px;top:326px;text-align:right;color:var(--white);font-size:19.5px;line-height:23px;font-weight:400}
  .intro em{font-style:italic}
  .phone{position:absolute;left:0;background:var(--ice);border-radius:0 26px 26px 0;display:flex;align-items:center;gap:6px;
    color:var(--ink);font-weight:800;font-size:26px;letter-spacing:-0.3px}
  .front .phone{top:422px;width:271px;height:48px;padding-left:20px}
  .back .phone{top:425px;width:251px;height:45px;padding-left:30px;font-size:24px}
  .phone svg{width:32px;height:32px;flex:none}
  .credentials-title{position:absolute;left:43px;top:124px;color:var(--ice);font-weight:800;font-size:24px;line-height:29px}
  .credentials-rule{position:absolute;left:195px;top:171px;width:110px;height:1px;background:var(--rule)}
  .credentials{position:absolute;left:43px;top:195px;list-style:none;color:var(--white);font-size:16px;line-height:19px}
  .credentials li{display:flex;gap:11px;margin-bottom:16px;align-items:center}
  .credentials svg{width:22px;height:24px;flex:none}
  .stamp-box{position:absolute;left:656px;top:20px;width:79px;height:90px;border:1px solid var(--rule)}
  .address-line{position:absolute;left:507px;width:222px;height:1px;background:var(--rule)}
</style>
</head>
<body>

<section class="card front">
  <div class="photo" role="img" aria-label="Photo of a woman in a knit hat and dark coat slipping and falling on an icy path"></div>
  <svg class="shape" viewBox="0 0 746 497" preserveAspectRatio="none">
    <path d="M0,230 L0,420 L150,420 C150,330 110,280 60,250 Z" fill="#ffffff" opacity="0.18"/>
    <path d="M565,0 L746,0 L746,497 L510,497 C500,470 470,450 460,420 C440,360 400,300 396,240 C392,190 400,160 430,135 Z" fill="var(--ink)"/>
  </svg>
  <div class="brand">The Frost Counsel</div>
  <h1 class="headline">
    <span class="light">Do you</span>
    <span class="light">handle</span>
    <span class="bold">Snow and</span>
    <span class="bold">ice related</span>
    <span class="bold ice">slip and</span>
    <span class="bold ice">falls?</span>
  </h1>
  <p class="intro">Darrel is one<br>of the top snow<br>industry experts in<br><em>the country!</em></p>
  <div class="phone">
    <svg viewBox="0 0 32 32"><circle cx="16" cy="16" r="14" fill="none" stroke="var(--ink)" stroke-width="2.4"/><path d="M11.5 8.5c1-.6 1.8-.3 2.3.6l1.3 2.6c.4.8.2 1.5-.5 2l-1 .7c.7 2 2 3.6 3.7 4.8l1-.8c.6-.5 1.4-.5 2 .1l2 2c.6.7.6 1.5-.2 2.2-1.3 1.2-3 1.5-4.6.7-3.8-2-6.7-5.5-7.8-9.7-.4-1.9.3-3.8 1.8-5.2z" fill="var(--ink)"/></svg>
    <span>(555) 284-3917</span>
  </div>
</section>

<section class="card back">
  <svg class="shape" viewBox="0 0 753 502" preserveAspectRatio="none">
    <path d="M0,0 L338,0 L450,112 C466,130 470,152 462,175 L341,502 L0,502 Z" fill="var(--ink-soft)"/>
    <path d="M0,0 L308,0 L412,115 C424,130 428,150 420,172 L290,502 L0,502 Z" fill="var(--ink)"/>
  </svg>
  <div class="brand">The Frost Counsel</div>
  <h2 class="credentials-title">Darrel's<br>Credentials</h2>
  <div class="credentials-rule"></div>
  <ul class="credentials">
    <li><svg viewBox="0 0 22 24"><path d="M11 1.5 20 6.5v11L11 22.5 2 17.5v-11z" fill="none" stroke="#fff" stroke-width="1.6"/><path d="M6.5 12.5l3 3 6-6.5" fill="none" stroke="#fff" stroke-width="2"/></svg><span>Accredited Winter<br>Practitioner (AWP)</span></li>
    <li><svg viewBox="0 0 22 24"><path d="M11 1.5 20 6.5v11L11 22.5 2 17.5v-11z" fill="none" stroke="#fff" stroke-width="1.6"/><path d="M6.5 12.5l3 3 6-6.5" fill="none" stroke="#fff" stroke-width="2"/></svg><span>Former ISO 9001 certified<br>snow company owner</span></li>
    <li><svg viewBox="0 0 22 24"><path d="M11 1.5 20 6.5v11L11 22.5 2 17.5v-11z" fill="none" stroke="#fff" stroke-width="1.6"/><path d="M6.5 12.5l3 3 6-6.5" fill="none" stroke="#fff" stroke-width="2"/></svg><span>Past WRTA board<br>member and chair</span></li>
    <li><svg viewBox="0 0 22 24"><path d="M11 1.5 20 6.5v11L11 22.5 2 17.5v-11z" fill="none" stroke="#fff" stroke-width="1.6"/><path d="M6.5 12.5l3 3 6-6.5" fill="none" stroke="#fff" stroke-width="2"/></svg><span>32 years in the<br>industry</span></li>
  </ul>
  <div class="phone">
    <svg viewBox="0 0 32 32"><circle cx="16" cy="16" r="14" fill="none" stroke="var(--ink)" stroke-width="2.4"/><path d="M11.5 8.5c1-.6 1.8-.3 2.3.6l1.3 2.6c.4.8.2 1.5-.5 2l-1 .7c.7 2 2 3.6 3.7 4.8l1-.8c.6-.5 1.4-.5 2 .1l2 2c.6.7.6 1.5-.2 2.2-1.3 1.2-3 1.5-4.6.7-3.8-2-6.7-5.5-7.8-9.7-.4-1.9.3-3.8 1.8-5.2z" fill="var(--ink)"/></svg>
    <span>(555) 284-3917</span>
  </div>
  <div class="stamp-box"></div>
  <div class="address-line" style="top:193px"></div>
  <div class="address-line" style="top:254px"></div>
  <div class="address-line" style="top:314px"></div>
  <div class="address-line" style="top:375px"></div>
  <div class="address-line" style="top:435px"></div>
</section>

</body>
</html>
```